2026 Marwick Dust Control Municipal Advertisement

I need a professional print advertisement designed for our road dust control business for a 2026 municipal/public works publication.

Our company manufactures, supplies, delivers and applies liquid road dust suppressant products to municipalities, contractors and commercial customers across Ontario.

I will upload:

* Our new truck/application photo to use as the main image
* Our advertisement from last year as a reference for the general style and information

I would like the new advertisement to look modern, professional, industrial and appropriate for municipal/public works decision-makers. The truck photo should be the main visual.

Please include the following wording:

MARWICK DUST CONTROL PRODUCTS
418307 Ontario Limited
Based in Clinton, Ontario

ROAD DUST CONTROL PRODUCTS

Manufacturer & Distributor of Liquid Road Dust Suppressants

AVAILABLE CONCENTRATIONS

35%
Liquid Calcium Magnesium Chloride Solution

30%

20%

Bulk Supply • Delivery • Road Application

Supplying Municipalities, Contractors & Commercial Customers Across Ontario

519-555-0187
dermarw417@quillpost.net

Please make “ROAD DUST CONTROL PRODUCTS” one of the most prominent pieces of wording.

The 35%, 30% and 20% product concentrations should also be large, clear and easy to read.

“MARWICK DUST CONTROL PRODUCTS” should be prominently branded, with “418307 Ontario Limited” smaller underneath.

Please do not overcrowd the advertisement. It should be easy for someone flipping through a municipal publication to understand within a few seconds what we sell and how to contact us.

```html
<!DOCTYPE html>
<html lang="en">
<head>
<meta charset="utf-8">
<title>Marwick Dust Control Products – Road Dust Control Advertisement</title>
<link rel="stylesheet" href="https://fonts.googleapis.com/css2?family=Russo+One&family=Exo+2:ital,wght@1,800&family=Arimo:wght@400;700&family=Saira:ital,wght@1,800&display=swap">
<style>
  :root {
    --ink: #000000;
    --white: #ffffff;
    --yellow: #f4e04d;
    --steel-light: #e6e8ea;
    --steel-dark: #7d8287;
    --panel-top: #3b3f44;
    --panel-bottom: #050607;
    --gravel: #b19a80;
    --gravel-dark: #8a7560;
    --grass: #58703a;
    --truck-blue: #2d48a0;
  }
  * { box-sizing: border-box; margin: 0; padding: 0; }
  html, body { width: 927px; height: 1200px; overflow: hidden; background: var(--ink); }
  .ad {
    position: relative; width: 927px; height: 1200px; overflow: hidden;
    background: var(--ink); color: var(--white);
    font-family: "Arimo", Arial, sans-serif;
  }
  .hero-photo {
    position: absolute; left: 0; top: 0; width: 927px; height: 920px;
    background:
      radial-gradient(ellipse 190px 420px at 470px 500px, rgba(45,72,160,.85) 0%, rgba(45,72,160,.55) 45%, rgba(45,72,160,0) 100%),
      linear-gradient(180deg, rgba(30,30,30,.35) 0%, rgba(0,0,0,0) 30%, rgba(0,0,0,0) 80%, rgba(0,0,0,.3) 100%),
      linear-gradient(90deg, var(--grass) 0%, var(--gravel-dark) 14%, var(--gravel) 38%, var(--gravel) 62%, var(--gravel-dark) 86%, var(--grass) 100%);
  }
  .headline {
    position: absolute; top: 32px; left: 0; width: 100%; text-align: center;
    font-family: "Russo One", "Arial Black", sans-serif;
    font-size: 66px; line-height: 64px; letter-spacing: 0.5px;
    text-shadow: 0 2px 6px rgba(0,0,0,.45);
  }
  .tagline {
    position: absolute; top: 160px; left: 0; width: 100%; text-align: center;
    font-family: "Exo 2", Arial, sans-serif; font-style: italic; font-weight: 800;
    font-size: 36px; line-height: 39px; letter-spacing: 0.3px;
    text-shadow: 0 2px 5px rgba(0,0,0,.5);
  }
  .brand-badge {
    position: absolute; left: 40px; top: 277px; width: 232px; height: 232px;
    border-radius: 50%;
    background: linear-gradient(135deg, var(--steel-light), var(--steel-dark) 55%, var(--steel-light));
    padding: 6px;
    box-shadow: 0 4px 10px rgba(0,0,0,.4);
  }
  .brand-badge__inner {
    width: 100%; height: 100%; border-radius: 50%;
    background: linear-gradient(180deg, var(--panel-top), var(--panel-bottom));
    display: flex; flex-direction: column; align-items: center; justify-content: center;
    text-align: center;
  }
  .brand-badge__name {
    font-family: "Russo One", "Arial Black", sans-serif;
    font-size: 22px; line-height: 27px; margin-top: 4px;
  }
  .brand-badge__meta { font-size: 14px; line-height: 17.5px; margin-top: 8px; }
  .products-heading {
    position: absolute; top: 770px; left: 0; width: 100%; text-align: center;
    font-family: "Russo One", "Arial Black", sans-serif;
    font-size: 18px; line-height: 22px; letter-spacing: 3px;
    text-shadow: 0 2px 5px rgba(0,0,0,.6);
  }
  .products { position: absolute; left: 0; top: 803px; width: 100%; height: 162px; }
  .product {
    position: absolute; top: 0; width: 270px; height: 162px;
    clip-path: polygon(14% 0, 100% 0, 86% 100%, 0 100%);
    background: linear-gradient(120deg, var(--steel-light), var(--steel-dark) 45%, var(--steel-light) 80%, var(--steel-dark));
  }
  .product__face {
    position: absolute; inset: 6px 8px;
    clip-path: polygon(14% 0, 100% 0, 86% 100%, 0 100%);
    background: linear-gradient(180deg, var(--panel-top), var(--panel-bottom));
    text-align: center; padding-top: 18px;
  }
  .product--35 { left: 91px; }
  .product--30 { left: 327px; }
  .product--20 { left: 563px; }
  .product__value {
    font-family: "Saira", "Arial Black", sans-serif; font-weight: 800; font-style: italic;
    font-size: 66px; line-height: 58px; color: var(--yellow);
  }
  .product__label { font-size: 16.5px; line-height: 19.5px; margin-top: 4px; }
  .services {
    position: absolute; top: 982px; left: 0; width: 100%; text-align: center;
    font-family: "Russo One", "Arial Black", sans-serif; font-size: 34px; line-height: 40px;
  }
  .services .dot { color: var(--yellow); }
  .reach {
    position: absolute; top: 1039px; left: 0; width: 100%; text-align: center;
    font-size: 19px; line-height: 22px;
  }
  .contact {
    position: absolute; top: 1116px; left: 0; width: 100%;
    display: flex; justify-content: center; align-items: center;
    font-weight: 700; font-size: 29px;
  }
  .contact__item { display: flex; align-items: center; gap: 12px; }
  .contact__icon { width: 37px; height: 37px; flex: none; }
  .contact__divider { width: 2px; height: 44px; background: var(--yellow); margin: 0 24px; }
</style>
</head>
<body>
<main class="ad">
  <div class="hero-photo" role="img" aria-label="Aerial photo of a blue tanker truck driving along a gravel road between grassy verges"></div>

  <h1 class="headline">ROAD DUST CONTROL<br>PRODUCTS</h1>
  <p class="tagline">Manufacturer &amp; Distributor of Liquid<br>Road Dust Suppressants</p>

  <div class="brand-badge">
    <div class="brand-badge__inner">
      <div class="brand-badge__name">MARWICK<br>DUST CONTROL<br>PRODUCTS</div>
      <div class="brand-badge__meta">418307 Ontario Limited<br>Based in Clinton,<br>Ontario</div>
    </div>
  </div>

  <h2 class="products-heading">AVAILABLE CONCENTRATIONS</h2>
  <section class="products" aria-label="Available concentrations">
    <div class="product product--35"><div class="product__face">
      <div class="product__value">35%</div>
      <div class="product__label">Liquid Calcium<br>Magnesium<br>Chloride Solution</div>
    </div></div>
    <div class="product product--30"><div class="product__face">
      <div class="product__value">30%</div>
      <div class="product__label">Liquid Calcium<br>Magnesium<br>Chloride Solution</div>
    </div></div>
    <div class="product product--20"><div class="product__face">
      <div class="product__value">20%</div>
      <div class="product__label">Liquid Calcium<br>Magnesium<br>Chloride Solution</div>
    </div></div>
  </section>

  <p class="services">Bulk Supply <span class="dot">•</span> Delivery <span class="dot">•</span> Road Application</p>
  <p class="reach">Supplying Municipalities, Contractors &amp; Commercial Customers Across Ontario</p>

  <div class="contact">
    <div class="contact__item">
      <svg class="contact__icon" viewBox="0 0 40 40" aria-hidden="true">
        <circle cx="20" cy="20" r="20" fill="#f4e04d"/>
        <path d="M13 10c1-1 2.5-1 3.3.2l2 3c.6 1 .4 2.2-.4 3l-1.4 1.2c1 2.3 2.8 4.1 5.1 5.1l1.2-1.4c.8-.8 2-1 3-.4l3 2c1.2.8 1.2 2.3.2 3.3l-1.6 1.6c-1.4 1.4-3.6 1.6-5.5.6-4.6-2.4-8.2-6-10.6-10.6-1-1.9-.8-4.1.6-5.5z" fill="#000"/>
      </svg>
      <span>519-555-0187</span>
    </div>
    <div class="contact__divider"></div>
    <div class="contact__item">
      <svg class="contact__icon" viewBox="0 0 40 40" aria-hidden="true">
        <circle cx="20" cy="20" r="20" fill="#f4e04d"/>
        <rect x="10" y="13" width="20" height="14" rx="1.5" fill="none" stroke="#000" stroke-width="2"/>
        <path d="M10.5 14l9.5 7.5 9.5-7.5M10.5 26.5l7-6M29.5 26.5l-7-6" fill="none" stroke="#000" stroke-width="1.8"/>
      </svg>
      <span>dermarw417@quillpost.net</span>
    </div>
  </div>
</main>
</body>
</html>
```